Product Setup Instructional Infographic/flyer

Converting product instructions into an infographic. Would prefer that the instructions fit on a 4x6 card, front and back, but a slightly larger size is acceptable as well.

Logo Text

Harbor Crest (Rebranding just as Harbor Crest, instead of Harbor Crest)

Font styles to use
Decorative

Colors

Designer to choose colors to be used in the design.

Requirements
Must have
• NA
Nice to have
• NA
Should not have
• NA

```html
<!DOCTYPE html>
<html lang="en">
<head>
<meta charset="utf-8">
<title>How to Cure Your Oak Barrel – Harbor Crest</title>
<link rel="stylesheet" href="https://fonts.googleapis.com/css2?family=Roboto+Condensed:wght@400;700&family=Arimo:wght@400&display=swap">
<style>
  :root {
    --navy: #141c42;
    --frame: #c9cbd6;
    --banner-red: #a11f2e;
    --white: #ffffff;
    --yellow: #f6da12;
    --step1: #8c1827;
    --step2: #a8233f;
    --step3: #dc3a55;
    --step4: #2d8c3e;
    --step5: #5cbb5e;
    --step6: #1a6c9d;
    --step7: #1fa8e0;
    --tip: #8c1827;
    --wood-light: #b26a2c;
    --wood-dark: #6e3a16;
  }
  * { box-sizing: border-box; margin: 0; padding: 0; }
  html, body { width: 800px; height: 1200px; overflow: hidden; background: var(--navy); }
  .canvas { position: relative; width: 800px; height: 1200px; background: var(--navy); }
  .frame { position: absolute; inset: 11px; border: 1px solid var(--frame); }
  .shapes { position: absolute; left: 0; top: 0; }
  .title {
    position: absolute; left: 218px; top: 44px; width: 360px; height: 80px;
    display: flex; align-items: center; justify-content: center; text-align: center;
    font-family: "Roboto Condensed", sans-serif; font-weight: 700; color: var(--white);
    font-size: 25px; line-height: 36px; text-transform: uppercase; letter-spacing: -0.3px;
  }
  .intro {
    position: absolute; left: 58px; top: 160px; width: 700px;
    font-family: "Roboto Condensed", sans-serif; color: var(--white);
    font-size: 13.4px; line-height: 20px;
  }
  .step { position: absolute; font-family: "Arimo", sans-serif; color: var(--yellow); font-size: 10.2px; line-height: 11.2px; }
  .step-title {
    font-family: "Roboto Condensed", sans-serif; font-weight: 700; color: var(--white);
    font-size: 17px; line-height: 20px; margin-bottom: 9px;
  }
  .step-1 { left: 470px; top: 310px; width: 156px; }
  .step-2 { left: 590px; top: 468px; width: 156px; }
  .step-2 .step-title { margin-left: 52px; }
  .step-3 { left: 574px; top: 704px; width: 122px; }
  .step-3 .step-title { margin-left: 8px; }
  .step-4 { left: 358px; top: 806px; width: 116px; }
  .step-4 .step-title { margin-left: 28px; }
  .step-5 { left: 118px; top: 700px; width: 156px; }
  .step-5 .step-title { margin-left: 68px; }
  .step-6 { left: 83px; top: 487px; width: 134px; }
  .step-6 .step-title { margin-left: 48px; margin-bottom: 4px; }
  .step-7 { left: 248px; top: 308px; width: 132px; }
  .step-7 .step-title { margin-left: 50px; }
  .tip-text {
    position: absolute; left: 302px; top: 1026px; width: 386px;
    font-family: "Arimo", sans-serif; color: var(--yellow); font-size: 10.2px; line-height: 11.2px;
  }
  .tip-text .step-title { margin-bottom: 10px; font-size: 17px; }
</style>
</head>
<body>
<div class="canvas">
  <div class="frame"></div>

  <svg class="shapes" width="800" height="1200" viewBox="0 0 800 1200">
    <defs>
      <path id="wedge" d="M269.1 274.2 A360 360 0 0 1 538.9 274.2 L468.4 448.5 A172 172 0 0 0 339.6 448.5 Z"/>
      <linearGradient id="wood" x1="0" y1="0" x2="1" y2="0">
        <stop offset="0" stop-color="var(--wood-dark)"/>
        <stop offset="0.5" stop-color="var(--wood-light)"/>
        <stop offset="1" stop-color="var(--wood-dark)"/>
      </linearGradient>
    </defs>

    <g class="title-banner" fill="var(--banner-red)">
      <polygon points="134,84 184,28 184,62 218,62 218,106 184,106 184,140"/>
      <polygon points="662,84 612,28 612,62 578,62 578,106 612,106 612,140"/>
      <rect x="218" y="44" width="360" height="80"/>
    </g>

    <g class="step-wedges" stroke="var(--white)" stroke-width="1.2">
      <use href="#wedge" fill="var(--step1)" transform="rotate(25.7 404 608)"/>
      <use href="#wedge" fill="var(--step2)" transform="rotate(77.1 404 608)"/>
      <use href="#wedge" fill="var(--step3)" transform="rotate(128.6 404 608)"/>
      <use href="#wedge" fill="var(--step4)" transform="rotate(180 404 608)"/>
      <use href="#wedge" fill="var(--step5)" transform="rotate(231.4 404 608)"/>
      <use href="#wedge" fill="var(--step6)" transform="rotate(282.9 404 608)"/>
      <use href="#wedge" fill="var(--step7)" transform="rotate(334.3 404 608)"/>
    </g>

    <rect class="barrel-art" x="300" y="476" width="212" height="248" rx="60" fill="url(#wood)" role="img" aria-label="Illustration of a wooden oak barrel with metal hoops and spigot"/>

    <g class="tip-bubble" fill="var(--tip)" stroke="var(--white)" stroke-width="1.2">
      <rect x="262" y="1008" width="444" height="144" rx="38"/>
      <polygon points="236,1068 263,1058 263,1078" stroke="none"/>
    </g>

    <rect class="barrel-art-small" x="76" y="988" width="144" height="176" rx="42" fill="url(#wood)" role="img" aria-label="Small illustration of a wooden oak barrel"/>
  </svg>

  <h1 class="title">A step by step guide on how<br>to cure your oak barrel</h1>

  <p class="intro">First, we would like to thank you for choosing Harbor Crest for your home spirit and wine-aging needs. We know you are very excited to use it and so are we. However, your barrel is NOT ready yet for use. You need to cure it first to get rid of the wood debris and make it watertight. Do not fret, we laid out an easy to follow step by step guide on how to ready your barrel for spirit and wine-aging.</p>

  <div class="step step-1"><h2 class="step-title">Step: 1</h2>Rinse and soak the spigot (wooden faucet) and the plug (or bung) in water for about half an hour.</div>
  <div class="step step-2"><h2 class="step-title">Step: 2</h2>While waiting, fill the barrel with water until it is half-full. Use your thumb to plug the holes, give it a good shake to get rid of wood chips and debris that might be trapped inside. Let the water out. You may repeat this process three to five times until you satisfied the barrel is thoroughly clean.</div>
  <div class="step step-3"><h2 class="step-title">Step: 3</h2>Plug the barrel with the spigot. You may tighten it securely with your hand. We advise not to use a hammer as it may crack the wood.</div>
  <div class="step step-4"><h2 class="step-title">Step: 4</h2>Place the barrel in a sink, tub, or any place that is OK to get wet.</div>
  <div class="step step-5"><h2 class="step-title">Step:5</h2>Using a funnel, fill the barrel with hot water until it is full. Leave the top hole open. Your barrel might leak, and that's OK. It is not watertight yet and this process will make the wood expand to seal the gaps.</div>
  <div class="step step-6"><h2 class="step-title">Step:6</h2>Leave the barrel this way until no more leakages can be seen. This means the wood has expanded and the gaps are sealed. This can take from 30 minutes to an entire week, depending on the size of the barrel.</div>
  <div class="step step-7"><h2 class="step-title">Step:7</h2>Drain the barrel and let it air dry for no more than four hours. After 4 hours, it is ready to be filled with any spirits or wine of your choice.</div>

  <div class="tip-text"><h2 class="step-title">Additional Tip:</h2>If you plan on aging different kinds of alcohol using the same barrel, you must cure the barrel again (Step 6) for three to five days. This will allow the barrel to absorb enough water and prevent the next batch of alcohol from being contaminated.</div>
</div>
</body>
</html>
```